The Bright Path Foundation

This is a non profit . We are a 501(c)(3) charitable organization in the United States. The organization is a volunteer based group providing basic healthcare to those living in underserved rural areas around the world. I have attached a brochure that provides some information about the organization. We are looking for a basic 5 page web page Page 1 Photos that fade into the next x 3 with mission statementPage 2 About us - details about bright path foundation. also introducing our Founders of the organization. Marlene Quist, M.D. Doria Lemke , FNP, Paula Dweck, FNP, Brent Lomax. ( will provide you info on each.Page 3 Projects coming up and futurePage 4 Get involved - Give a donation, Volunteer, Corporate supportPage 5 Support us and contact us with a message box.We mainly work in South America but anticipate trave to South Africa in the near future. Colors bright with emphasis on Reds and Purples. I have attached some photos and ideas. You can use or not use ok to use something similar if you so like

Target Market(s)

People interested in volunteering time or money to overseas medical work. NOT a religious base

Colors
876aae
ec1f27
f37022
9bcb3c

Requirements
Must have
• Colorful pictures nature, brings out emotion, colorful, children from various parts of the world, animals.
• Tried to down load some pictures but would not go thru.

```html
<!DOCTYPE html>
<html lang="en">
<head>
<meta charset="utf-8">
<title>The Bright Path Foundation – About Us</title>
<link href="https://fonts.googleapis.com/css2?family=Crimson+Pro:wght@600;700&family=Raleway:wght@400;500;600;700&display=swap" rel="stylesheet">
<style>
:root{
  --purple:#876aae;
  --purple-deep:#6d559a;
  --purple-line:#9b82c2;
  --orange:#f37022;
  --ink:#2d2d2d;
  --body:#4a4a4a;
  --white:#ffffff;
  --nav-ink:#333333;
}
*{margin:0;padding:0;box-sizing:border-box}
html,body{width:1200px;height:3451px;overflow:hidden}
body{position:relative;background:var(--white);font-family:"Raleway",sans-serif;color:var(--body)}
.abs{position:absolute}

/* header */
.site-header{position:absolute;left:0;top:0;width:1200px;height:75px;background:var(--white);border-bottom:2px solid var(--purple-line);z-index:3}
.brand{position:absolute;left:187px;top:0;width:155px;height:105px;background:var(--white);box-shadow:0 2px 6px rgba(0,0,0,.12);display:flex;flex-direction:column;align-items:center;justify-content:center;gap:6px}
.brand-dot{width:30px;height:30px;border-radius:50%;background:var(--purple)}
.brand-name{font-family:"Crimson Pro",serif;font-weight:600;font-size:14px;color:var(--purple);text-align:center;line-height:1.1}
.nav{position:absolute;top:32px;font-size:11px;font-weight:500;color:var(--nav-ink);letter-spacing:.3px}
.nav-active{border-bottom:1px solid var(--nav-ink);padding-bottom:8px;color:#777}
.donate{position:absolute;left:927px;top:25px;width:85px;height:29px;border:2px solid var(--purple);border-radius:3px;font-size:9px;font-weight:700;letter-spacing:1.5px;color:var(--purple);display:flex;align-items:center;justify-content:center}

/* hero */
.hero{position:absolute;left:0;top:75px;width:1200px;height:501px;background:linear-gradient(180deg,#8fb6d3 0%,#6f9bc0 35%,#5d7fa3 55%,#5a4d86 78%,#4b3466 100%)}
.hero-kicker{position:absolute;left:248px;top:185px;color:var(--white);font-size:12px;font-weight:700;letter-spacing:2px;display:flex;align-items:center;gap:8px}
.hero-title{position:absolute;left:247px;top:215px;font-family:"Crimson Pro",serif;font-weight:700;font-size:54px;color:var(--white)}
.hero-text{position:absolute;left:247px;top:290px;width:470px;font-size:19px;line-height:27px;color:var(--white)}
.hero-status{position:absolute;left:778px;top:414px;color:var(--white);font-weight:700}
.hero-status .label{font-size:12px;letter-spacing:1.6px;border-bottom:2px solid var(--white);padding-bottom:3px;display:inline-block}
.hero-status .place{font-size:11px;letter-spacing:.8px;margin-top:14px;border-bottom:2px solid var(--white);padding-bottom:5px;display:inline-block}

/* founders */
.section-title{position:absolute;left:0;top:646px;width:1200px;text-align:center;font-family:"Crimson Pro",serif;font-weight:600;font-size:35px;color:var(--ink)}
.section-rule{position:absolute;left:571px;top:693px;width:59px;height:3px;background:var(--orange)}
.founder-backdrop{position:absolute;width:239px;height:443px}
.founder-frame{position:absolute;width:199px;height:258px;background:var(--white)}
.founder-photo{position:absolute;width:177px;height:227px}
.founder-name{position:absolute;font-size:15px;font-weight:600;color:var(--ink)}
.founder-role{position:absolute;font-size:10.5px;letter-spacing:1.5px;color:var(--ink)}
.founder-bio{position:absolute;width:410px;font-size:12.4px;line-height:22.5px;color:var(--body)}
.founder-bio p+p{margin-top:22.5px}

/* footer */
.site-footer{position:absolute;left:0;top:3184px;width:1200px;height:224px;background:var(--purple)}
.footer-bar{position:absolute;left:0;top:3408px;width:1200px;height:43px;background:var(--purple-deep);color:var(--white);font-size:9px}
.footer-heading{position:absolute;font-size:15px;font-weight:600;color:var(--white)}
.footer-text{position:absolute;font-size:10.5px;line-height:21px;color:var(--white)}
.footer-menu{position:absolute;left:560px;top:3263px;width:120px;text-align:center;font-size:11px;line-height:23px;color:var(--white)}
.social{position:absolute;top:3262px;width:21px;height:21px;border-radius:50%;background:var(--white)}
</style>
</head>
<body>

<header class="site-header">
  <div class="brand"><span class="brand-dot"></span><span class="brand-name">Bright Path Foundation</span></div>
  <span class="nav nav-active" style="left:587px">HOME</span>
  <span class="nav" style="left:644px">ABOUT US</span>
  <span class="nav" style="left:723px">OUR PROJECTS</span>
  <span class="nav" style="left:826px">GET INVOLVED</span>
  <span class="donate">DONATE</span>
</header>

<section class="hero" role="img" aria-label="Snowy mountain range above a meadow of purple wildflowers"></section>
<div class="hero-kicker">ABOUT US
  <svg width="22" height="12" viewBox="0 0 22 12"><path d="M0 6h20M15 1l5 5-5 5" fill="none" stroke="#fff" stroke-width="1.6"/></svg>
</div>
<h1 class="hero-title">We Are</h1>
<p class="hero-text">A 501(c)(3) charitable organization in the United States. The organization is a volunteer based group providing basic healthcare to those living in underserved rural areas around the world.</p>
<div class="hero-status"><span class="label">CURRENTLY WORKING IN</span><br><span class="place">South America</span></div>

<h2 class="section-title">Our Founders</h2>
<div class="section-rule"></div>

<!-- founder 1 -->
<div class="founder-backdrop" style="left:187px;top:755px;background:linear-gradient(160deg,#4f7fd6,#7da4ea 50%,#3b62b8)" role="img" aria-label="Blue hydrangea blossoms"></div>
<div class="founder-frame" style="left:309px;top:850px"></div>
<div class="founder-photo" style="left:321px;top:865px;background:linear-gradient(180deg,#7a7e86,#4f5258)" role="img" aria-label="Portrait of Marlene Quist"></div>
<h3 class="founder-name" style="left:574px;top:779px">Marlene Quist</h3>
<span class="founder-role" style="left:574px;top:808px">M.D. ( CO - FOUNDER)</span>
<div class="founder-bio" style="left:574px;top:833px">
<p>Marlene Quist grew up just outside of San Francisco. She moved to Colorado in 2000 after completing her medical residency at Alder State University in Morgantown West Virginia. She is board certified in both Internal Medicine and Pediatrics. Marlene's work currently has her traveling between the Boulder/Denver area and Trinidad, Colorado. In 2013 she founded Pine Ridge Health Center which is a primary care clinic providing healthcare services to those living in rural Southern Colorado. In 2017 she started and now operates Pine Ridge Health Center Palliative Care and Hospice which is a fully accredited non-profit providing end of life care to patients coping with a chronic and/or terminal illness.</p>
<p>Marlene enjoys long-distance running, sea kayaking, travel and international medicine. She also spends time rescuing aging, abused and neglected animals and has an array of dogs, cats, donkeys and, on occasion, goats</p>
</div>

<!-- founder 2 -->
<h3 class="founder-name" style="left:187px;top:1283px">Doria Lemke</h3>
<span class="founder-role" style="left:187px;top:1312px">FNP ( CO - FOUNDER)</span>
<div class="founder-bio" style="left:187px;top:1337px">
<p>Doria Lemke is a Nurse Practitioner who is currently practicing in her home state of Colorado. Doria has spent many years working with underserved populations and has a passion for serving in her global community. Doria graduated from Front Range University with a Bachelor's in Nursing. Doria initially worked in the oncology field but soon determined that she desired a more on-going relationship with the people that she cared for. With relationship in mind,</p>
<p>Doria became a part of a local federally qualified health center. Doria's desire was to use primary intervention and education, to add her own effort to, improve the health of her local community. After several years of working as a nurse in the community, Doria decided to return to school to become a nurse practitioner. Upon graduation from the Larkspur University Nurse Practitioner Rural and Underserved program Doria began practice at the federally qualified health center where she had become a part of the community and has continued to build relationships within that capacity. Doria is fluent in Spanish.</p>
<p>She also runs a local soup kitchen on the weekends, has participated on several medical missions to Peru as well as Mexico. In her spare time, Doria enjoys reading, traveling, spending time with her husband, six children, grandson and boxer pup.</p>
</div>
<div class="founder-backdrop" style="left:773px;top:1310px;background:linear-gradient(160deg,#c4121a,#e0242b 50%,#9c0c12)" role="img" aria-label="Red roses"></div>
<div class="founder-frame" style="left:692px;top:1402px"></div>
<div class="founder-photo" style="left:699px;top:1418px;background:linear-gradient(180deg,#b3241e,#3d5a9a)" role="img" aria-label="Portrait of Doria Lemke"></div>

<!-- founder 3 -->
<div class="founder-backdrop" style="left:187px;top:1953px;background:linear-gradient(160deg,#e8708f,#f3a3b9 45%,#d2486d 70%,#3a1820)" role="img" aria-label="Pink paper roses"></div>
<div class="founder-frame" style="left:309px;top:2049px"></div>
<div class="founder-photo" style="left:321px;top:2064px;background:linear-gradient(180deg,#7d8a63,#c79d7c 60%,#b58aa2)" role="img" aria-label="Portrait of Paula Dweck"></div>
<h3 class="founder-name" style="left:575px;top:1907px">Paula Dweck</h3>
<span class="founder-role" style="left:575px;top:1937px">FNP ( CO - FOUNDER)</span>
<div class="founder-bio" style="left:575px;top:1962px">
<p>Paula is committed to live her life in service to others and make a global difference in the world. She was born in Canary Islands Spain and has traveled and lived in many areas of the world. Through these experiences, Paula developed a deep passion for charitable work and helping people without access to health care. Her service to others started in 1995 when she joined The Willowmere Outreach League.</p>
<p>While there, she successfully led a first aid training seminar for local community health leaders in the remote jungles of Guatemala. She made it her goal to instruct local school members in teaching techniques as well as to deliver talks on health and nutritional education to indigenous women and children. Paula returned to the United States to raise her twin boys and dedicated herself to helping less fortunate individuals in the US. As Assistant Medical Director at a community clinic in Colorado, Paula strives to make the lives of her patients better. Additionally, Paula has participated in several medical missions around the world, most recently in the remote Sacred Valley of Peru. For her, getting exposure to new people and new cultures is both thrilling and gratifying. When she isn't busy helping others, Paula enjoys spending time with her children, traveling, hiking mountains (such as Mt Rainer and Kilimanjaro) and her four cats .</p>
</div>

<!-- founder 4 -->
<h3 class="founder-name" style="left:187px;top:2485px">Brent Lomax</h3>
<span class="founder-role" style="left:187px;top:2515px">( CO - FOUNDER)</span>
<div class="founder-bio" style="left:187px;top:2540px">
<p>Brent Lomax is a stylist and make-up artist in Boulder ,Colorado. He has always had a passion for helping others. Upon finishing high school, he obtained his Certified Nursing Assistant through Cumberland Technical College. He worked in a private nursing home for 3 years where his duties were to care for his patients by feeding, changing, bathing, and when ill keeping a close eye on their vital signs. He continued to become a Certified Physical Therapy Assistant where he then was responsible for his patients' rehabilitation after surgeries and daily exercises.</p>
<p>Brent has always had an artistic side and became a stylist. He started his own business in 2013, Brent Lomax INC. He has also assisted on Medical mission trips to the Sacred Valley, Peru for several years. He is active in charity work in Boulder, Colorado and volunteers for a HIV outreach and preventive care organization.</p>
<p>With his free time he enjoys traveling to Mexico, hiking the beautiful mountains of Colorado and spending time with his two dogs.</p>
</div>
<div class="founder-backdrop" style="left:773px;top:2513px;background:linear-gradient(160deg,#5a2a9a,#8a4fd0 50%,#3b1670)" role="img" aria-label="Purple phlox flowers"></div>
<div class="founder-frame" style="left:692px;top:2607px"></div>
<div class="founder-photo" style="left:699px;top:2622px;background:linear-gradient(180deg,#6a4fd2,#4a2a9a)" role="img" aria-label="Portrait of Brent Lomax"></div>

<footer class="site-footer"></footer>
<h4 class="footer-heading" style="left:249px;top:3229px">Contact us</h4>
<div class="footer-text" style="left:249px;top:3262px">info@brightpathfoundation.or<br>www.BrightPathFoundation.org<br>Phone: 1-555-014-2290</div>
<h4 class="footer-heading" style="left:560px;top:3229px;width:120px;text-align:center">Menu</h4>
<div class="footer-menu">Home<br>Our Projects<br>Get Involved<br>About us</div>
<h4 class="footer-heading" style="left:857px;top:3229px">Follow us on</h4>
<span class="social" style="left:857px"></span>
<span class="social" style="left:892px"></span>
<span class="social" style="left:927px"></span>
<div class="footer-bar">
  <span class="abs" style="left:250px;top:16px">copyright 2019 bright&amp;path</span>
  <span class="abs" style="left:794px;top:17px">Donor Terms</span>
  <span class="abs" style="left:890px;top:16px">Privacy policy</span>
</div>

</body>
</html>
```